Signage for a store*

logo on the two sides of the sign
in the middle is the name of the store witch is KORVELO
at the bottom of the two logos, one side for location/address and the other side is contact details phone number is 718-392-6170 address is 7342 THE SIGN WILL BEE 15 FEET BY 4 FEET I WOULD LIKE THAT THE
BACKGROUND OF THE SIGN SHOULD HAVE A NICE COLOR BASE
THAT GOES FOR A WINE STORE

```html
<!DOCTYPE html>
<html lang="en">
<head>
<meta charset="utf-8">
<title>KORVELO – Store Sign</title>
<link rel="stylesheet" href="https://fonts.googleapis.com/css2?family=Montserrat:wght@400;700;800&display=swap">
<style>
  :root {
    --page-grey: #e2e2e4;
    --wine-deep: #6a0a16;
    --wine-mid: #8c1420;
    --wine-glow: #a11b28;
    --gold: #d9b98a;
    --white: #ffffff;
    --caption: #222222;
  }
  html, body {
    margin: 0;
    padding: 0;
    width: 1200px;
    height: 424px;
    overflow: hidden;
    background: var(--page-grey);
    font-family: "Montserrat", Arial, sans-serif;
  }
  .canvas {
    position: relative;
    width: 1200px;
    height: 424px;
  }
  .sign {
    position: absolute;
    left: 69px;
    top: 56px;
    width: 1062px;
    height: 283px;
    background: radial-gradient(ellipse 55% 60% at 50% 50%, var(--wine-glow) 0%, var(--wine-mid) 55%, var(--wine-deep) 100%);
    box-shadow: 0 3px 10px rgba(0, 0, 0, 0.28);
  }
  .brand-mark {
    position: absolute;
    top: 50px;
    width: 150px;
    height: 190px;
    display: flex;
    flex-direction: column;
    align-items: center;
    justify-content: center;
    gap: 14px;
  }
  .brand-mark--left { left: 56px; }
  .brand-mark--right { right: 49px; }
  .brand-mark__dot {
    width: 34px;
    height: 34px;
    border: 2px solid var(--gold);
    border-radius: 50%;
    box-sizing: border-box;
  }
  .brand-mark__name {
    color: var(--gold);
    font-weight: 400;
    font-size: 25px;
    letter-spacing: 1px;
    line-height: 1;
  }
  .store-name {
    position: absolute;
    left: 0;
    right: 0;
    top: 62px;
    margin: 0;
    text-align: center;
    color: var(--white);
    font-weight: 800;
    font-size: 118px;
    line-height: 1;
    letter-spacing: -2px;
  }
  .contact-line {
    position: absolute;
    left: 0;
    right: 0;
    top: 199px;
    display: flex;
    justify-content: center;
    align-items: center;
    gap: 14px;
    color: var(--white);
    font-weight: 800;
    font-size: 20px;
    line-height: 1;
  }
  .contact-line__divider {
    width: 12px;
    height: 26px;
    display: block;
  }
  .caption {
    position: absolute;
    left: 0;
    right: 0;
    top: 366px;
    text-align: center;
    color: var(--caption);
    font-size: 10px;
    font-weight: 400;
  }
</style>
</head>
<body>
<main class="canvas">
  <section class="sign" aria-label="KORVELO store sign">
    <div class="brand-mark brand-mark--left">
      <span class="brand-mark__dot"></span>
      <span class="brand-mark__name">KORVELO</span>
    </div>

    <h1 class="store-name">KORVELO</h1>

    <p class="contact-line">
      <span class="contact-line__address">7342 Marlow Ave. Brooklyn, N.Y. 11209</span>
      <svg class="contact-line__divider" viewBox="0 0 12 26" aria-hidden="true">
        <ellipse cx="6" cy="13" rx="5" ry="11" fill="none" stroke="var(--gold)" stroke-width="1.4"/>
      </svg>
      <span class="contact-line__phone">718-392-6170</span>
    </p>

    <div class="brand-mark brand-mark--right">
      <span class="brand-mark__dot"></span>
      <span class="brand-mark__name">KORVELO</span>
    </div>
  </section>

  <p class="caption">Design Concept 1</p>
</main>
</body>
</html>
```